Business Card Design

I need a business card for a new company based in Australia called "MedLinkora".

Its a cloud program for GPs that allows them to search for the specialist they require using a simple user friendly tool.

I would like the colours to match those in the program (the colours in the logo attached).

The final design should reflect the programs clarity, ease of use and professionalism.

Target Market(s)

GPs and other Health Professionals

Industry/Entity Type

Business

Contact Information for Business Card

MedLinkora; The Trusted Clinician Index; Marla Ostrove CEO; 0438215906; marla@medlinkora.example; www.medlinkora.example

Requirements
Must have
• Must have the logo attached; the web address and my name and phone number
Nice to have
• the slogan "The Trusted Clinician Index"

```html
<!DOCTYPE html>
<html lang="en">
<head>
<meta charset="utf-8">
<title>MedLinkora Business Card</title>
<link rel="stylesheet" href="https://fonts.googleapis.com/css2?family=Questrial&family=Mulish:wght@700&display=swap">
<style>
  :root {
    --page-bg: #eceeee;
    --brand-cyan: #1ab4e6;
    --tagline-grey: #a3a3a3;
    --ink: #333333;
    --ink-strong: #2a2a2a;
    --card-edge: #c6c6c6;
    --card-light: #ffffff;
  }
  html, body {
    margin: 0;
    padding: 0;
    width: 1112px;
    height: 1200px;
    overflow: hidden;
    background: var(--page-bg);
  }
  .canvas {
    position: relative;
    width: 1112px;
    height: 1200px;
    font-family: "Questrial", sans-serif;
  }
  .card {
    position: absolute;
    left: 134px;
    width: 845px;
    height: 490px;
    overflow: hidden;
    background: linear-gradient(90deg, var(--card-edge) 0%, #f3f3f3 30%, var(--card-light) 55%, #f1f1f1 80%, var(--card-edge) 100%);
    box-shadow: 0 6px 14px rgba(0, 0, 0, 0.18);
  }
  .card--front { top: 78px; }
  .card--back { top: 651px; }
  .card__wave {
    position: absolute;
    left: 0;
    top: 0;
    width: 845px;
    height: 490px;
  }
  .brand {
    position: absolute;
    left: 86px;
    top: 96px;
    display: flex;
    align-items: center;
    gap: 18px;
  }
  .brand__mark {
    width: 40px;
    height: 40px;
    background: var(--brand-cyan);
    flex: none;
  }
  .brand__name {
    margin: 0;
    font-size: 64px;
    font-weight: 400;
    line-height: 1;
    color: var(--brand-cyan);
  }
  .brand-tagline {
    position: absolute;
    left: 86px;
    top: 196px;
    margin: 0;
    font-size: 33px;
    letter-spacing: 1px;
    color: var(--tagline-grey);
  }
  .web-address,
  .service-line {
    position: absolute;
    left: 0;
    width: 845px;
    margin: 0;
    text-align: center;
    font-size: 37px;
    color: var(--ink);
  }
  .web-address { top: 357px; }
  .service-line { top: 367px; }
  .holder-name {
    position: absolute;
    left: 214px;
    top: 58px;
    margin: 0;
    font-family: "Mulish", sans-serif;
    font-weight: 700;
    font-size: 34px;
    color: var(--ink-strong);
  }
  .contact-list {
    position: absolute;
    left: 214px;
    top: 136px;
    margin: 0;
    padding: 0;
    list-style: none;
  }
  .contact-list__item {
    display: flex;
    align-items: center;
    height: 68px;
    font-size: 37px;
    color: var(--ink);
  }
  .contact-list__icon {
    width: 24px;
    height: 26px;
    margin-right: 18px;
    flex: none;
  }
</style>
</head>
<body>
<main class="canvas">
  <section class="card card--front">
    <svg class="card__wave" viewBox="0 0 845 490" aria-hidden="true">
      <defs>
        <linearGradient id="band-blue-front" x1="0" y1="0" x2="0" y2="1">
          <stop offset="0" stop-color="#1ab4e6"/>
          <stop offset="0.45" stop-color="#7fd3f1"/>
          <stop offset="1" stop-color="#ffffff"/>
        </linearGradient>
        <linearGradient id="band-silver-front" x1="0" y1="0" x2="1" y2="0">
          <stop offset="0" stop-color="#8e8e8e"/>
          <stop offset="0.45" stop-color="#f4f4f4"/>
          <stop offset="0.7" stop-color="#bdbdbd"/>
          <stop offset="1" stop-color="#7d7d7d"/>
        </linearGradient>
      </defs>
      <path d="M0 318 Q422 282 845 318 L845 490 L0 490 Z" fill="url(#band-blue-front)"/>
      <path d="M0 309 Q422 273 845 309 L845 318 Q422 282 0 318 Z" fill="url(#band-silver-front)"/>
    </svg>
    <div class="brand">
      <span class="brand__mark" aria-hidden="true"></span>
      <h1 class="brand__name">MedLinkora</h1>
    </div>
    <p class="brand-tagline">The Trusted Clinician Index</p>
    <p class="web-address">www.medlinkora.example</p>
  </section>

  <section class="card card--back">
    <svg class="card__wave" viewBox="0 0 845 490" aria-hidden="true">
      <defs>
        <linearGradient id="band-blue-back" x1="0" y1="0" x2="0" y2="1">
          <stop offset="0" stop-color="#1ab4e6"/>
          <stop offset="0.45" stop-color="#7fd3f1"/>
          <stop offset="1" stop-color="#ffffff"/>
        </linearGradient>
        <linearGradient id="band-silver-back" x1="0" y1="0" x2="1" y2="0">
          <stop offset="0" stop-color="#8e8e8e"/>
          <stop offset="0.45" stop-color="#f4f4f4"/>
          <stop offset="0.7" stop-color="#bdbdbd"/>
          <stop offset="1" stop-color="#7d7d7d"/>
        </linearGradient>
      </defs>
      <path d="M0 324 Q422 288 845 324 L845 490 L0 490 Z" fill="url(#band-blue-back)"/>
      <path d="M0 315 Q422 279 845 315 L845 324 Q422 288 0 324 Z" fill="url(#band-silver-back)"/>
    </svg>
    <h2 class="holder-name">Marla Ostrove CEO</h2>
    <ul class="contact-list">
      <li class="contact-list__item">
        <svg class="contact-list__icon" viewBox="0 0 24 26" aria-hidden="true">
          <rect x="5" y="1.5" width="14" height="23" rx="2.5" fill="none" stroke="var(--brand-cyan)" stroke-width="2"/>
          <line x1="10" y1="21" x2="14" y2="21" stroke="var(--brand-cyan)" stroke-width="1.6"/>
        </svg>
        0438215906
      </li>
      <li class="contact-list__item">
        <svg class="contact-list__icon" viewBox="0 0 24 26" aria-hidden="true">
          <rect x="1.5" y="6" width="21" height="14" fill="none" stroke="var(--brand-cyan)" stroke-width="2"/>
          <polyline points="1.5,6 12,14 22.5,6" fill="none" stroke="var(--brand-cyan)" stroke-width="2"/>
        </svg>
        marla@medlinkora.example
      </li>
    </ul>
    <p class="service-line">Fast, simple specialist search for GPs</p>
  </section>
</main>
</body>
</html>
```